Tidewater Ridge Podiatry

Please design a flyer using the same layout/font/colours ect as the business card (attached) please make the flyer with curved corners.
Front of DL flyer: (vertical)
Business name & logo (same as card attached)
Treatments include:
-foot, ankle & leg pain
-heel pain
-nail care
-corn & callus treatment
-bunion advice
-mechanical assessments
-orthotics
-nail surgery

Consulting within 'Bellwind Family Pharmacy' ApolloBay.
47-49 Tillbrook Parade, Marrowcliff Bay.
Call for appointments: 0411 837 260

Email:tidewaterridgepodiatry@pelmornmail.net

Reverse of flyer (horizontal)
Business name & logo

Derek Hollins
B.Pod.
B.App.Sci (HM)
NWMBQ Reg: Pod 0007384251

0422 716 308

RHS,KMB & LWF registered provider
Private Health Insurance-ancillaries cover.

```html
<!DOCTYPE html>
<html lang="en">
<head>
<meta charset="utf-8">
<title>Tidewater Ridge Podiatry – Flyer and Card</title>
<link rel="stylesheet" href="https://fonts.googleapis.com/css2?family=Questrial&family=Nunito:wght@700;800&display=swap">
<style>
  :root{
    --teal:#3fb4c7;
    --teal-deep:#2fa3b6;
    --charcoal:#58595b;
    --slate:#8e9092;
    --ink:#1d1d1f;
    --paper:#ffffff;
    --canvas:#ffffff;
  }
  *{box-sizing:border-box;margin:0;padding:0}
  html,body{width:832px;height:1200px;overflow:hidden;background:var(--canvas)}
  body{position:relative;font-family:"Questrial",sans-serif}

  /* ---------- DL flyer ---------- */
  .flyer{
    position:absolute;left:225px;top:22px;width:378px;height:757px;
    border-radius:22px;overflow:hidden;background:var(--paper);
    box-shadow:0 0 0 1px #e4e4e4;
  }
  .flyer__waves{position:absolute;inset:0;width:100%;height:100%}
  .brand{position:absolute;left:0;right:0;text-align:center}
  .brand__dot{display:block;margin:0 auto 14px;width:58px;height:58px;border-radius:50%;background:var(--teal)}
  .brand__name{font-family:"Questrial",sans-serif;color:var(--teal);font-size:25px;line-height:1.15}
  .flyer .brand{top:26px}

  .treatments{position:absolute;left:24px;top:262px;list-style:none;color:var(--paper);font-size:17px;line-height:25px}
  .treatments li{position:relative;padding-left:14px}
  .treatments li::before{content:"";position:absolute;left:0;top:9px;width:8px;height:8px;border-radius:50%;background:var(--charcoal)}

  .rule{position:absolute;left:22px;width:240px;height:1px;background:rgba(255,255,255,.55)}
  .rule--top{top:466px}
  .rule--bottom{top:560px}

  .venue{position:absolute;left:22px;top:474px;width:250px;text-align:center;font-family:"Nunito",sans-serif;font-weight:700;font-size:15.5px;line-height:21px;color:var(--paper)}
  .venue__name{color:var(--charcoal)}
  .address{position:absolute;left:22px;top:534px;font-size:11.5px;color:var(--paper)}

  .cta{position:absolute;left:0;right:0;top:590px;text-align:center;font-family:"Nunito",sans-serif;font-weight:800}
  .cta__label{color:var(--charcoal);font-size:26px;line-height:32px}
  .cta__phone{color:var(--paper);font-size:40px;line-height:48px;letter-spacing:.5px}

  .flyer__footer{position:absolute;left:0;right:0;bottom:0;height:48px;display:flex;align-items:center;justify-content:center;gap:8px;color:var(--paper);font-size:14px}
  .icon{flex:none}

  /* ---------- Business card ---------- */
  .card{
    position:absolute;left:39px;top:801px;width:756px;height:383px;
    border-radius:24px;overflow:hidden;background:var(--paper);
    box-shadow:0 0 0 1px #e4e4e4;
  }
  .card__shapes{position:absolute;inset:0;width:100%;height:100%}
  .card .brand{left:30px;right:auto;width:260px;top:128px}
  .card .brand__dot{background:var(--paper);width:52px;height:52px}
  .card .brand__name{color:var(--paper);font-size:23px}

  .registration{position:absolute;right:32px;top:34px;text-align:right;color:var(--teal)}
  .registration__number{font-size:15px;letter-spacing:.5px;margin-bottom:10px}
  .registration__cover{font-size:12px;line-height:17px;letter-spacing:.3px}

  .practitioner{position:absolute;right:32px;top:188px;text-align:right}
  .practitioner__name{font-size:27px;letter-spacing:1.5px;color:var(--ink)}
  .practitioner__quals{font-size:18px;letter-spacing:1px;color:var(--ink);margin-top:12px}

  .contact{position:absolute;right:28px;top:296px;text-align:right;color:var(--ink)}
  .contact__row{display:flex;align-items:center;justify-content:flex-end;gap:12px;font-size:19px;letter-spacing:1px;height:36px}
  .contact__row--email{font-size:17.5px;letter-spacing:.4px}
</style>
</head>
<body>

<!-- Front: vertical DL flyer -->
<section class="flyer" aria-label="Flyer front">
  <svg class="flyer__waves" viewBox="0 0 378 757" preserveAspectRatio="none" aria-hidden="true">
    <path d="M0,222 C120,188 260,180 378,196 V757 H0 Z" fill="var(--charcoal)"/>
    <path d="M0,238 C130,210 270,212 378,250 V757 H0 Z" fill="var(--teal)"/>
    <path d="M0,712 C110,676 270,672 378,700 V757 H0 Z" fill="var(--paper)"/>
    <path d="M0,724 C120,700 260,700 378,720 V757 H0 Z" fill="var(--charcoal)"/>
    <path d="M300,220 C390,300 300,420 330,560 C345,640 378,660 378,660 V240 Z" fill="rgba(255,255,255,.14)"/>
  </svg>

  <div class="brand">
    <span class="brand__dot"></span>
    <div class="brand__name">Tidewater Ridge<br>Podiatry</div>
  </div>

  <ul class="treatments">
    <li>foot, ankle &amp; leg pain</li>
    <li>heel pain</li>
    <li>nail care</li>
    <li>corn &amp; callus treatment</li>
    <li>bunion advice</li>
    <li>mechanical assessments</li>
    <li>orthotics</li>
    <li>nail surgery</li>
  </ul>

  <div class="rule rule--top"></div>
  <p class="venue">Consulting within <span class="venue__name">'Bellwind Family Pharmacy'</span> MarrowcliffBay</p>
  <p class="address">47-49 Tillbrook Parade, Marrowcliff Bay</p>
  <div class="rule rule--bottom"></div>

  <div class="cta">
    <div class="cta__label">Call for appointments</div>
    <div class="cta__phone">0411 837 260</div>
  </div>

  <div class="flyer__footer">
    <svg class="icon" width="24" height="17" viewBox="0 0 24 17" aria-hidden="true">
      <rect x="1" y="1" width="22" height="15" fill="none" stroke="#fff" stroke-width="2"/>
      <path d="M1,1 L12,10 L23,1" fill="none" stroke="#fff" stroke-width="2"/>
    </svg>
    <span>tidewaterridgepodiatry@pelmornmail.net</span>
  </div>
</section>

<!-- Reverse: horizontal card -->
<section class="card" aria-label="Flyer reverse">
  <svg class="card__shapes" viewBox="0 0 756 383" preserveAspectRatio="none" aria-hidden="true">
    <path d="M210,0 H335 C405,110 385,270 318,383 H280 C345,260 345,90 250,0 Z" fill="var(--charcoal)"/>
    <path d="M335,0 C420,90 410,260 340,383 H326 C390,260 400,110 320,0 Z" fill="rgba(142,144,146,.35)"/>
    <path d="M0,0 H250 C345,90 345,260 280,383 H0 Z" fill="var(--teal)"/>
  </svg>

  <div class="brand">
    <span class="brand__dot"></span>
    <div class="brand__name">Tidewater Ridge<br>Podiatry</div>
  </div>

  <div class="registration">
    <p class="registration__number">NWMBQ REG: POD 0007384251</p>
    <p class="registration__cover">RHS,KMB &amp; LWF REGISTERED PROVIDER<br>PRIVATE HEALTH INSURANCE-ANCILLARIES COVER.</p>
  </div>

  <div class="practitioner">
    <p class="practitioner__name">DEREK HOLLINS</p>
    <p class="practitioner__quals">B.Pod B App Sci (HM)</p>
  </div>

  <div class="contact">
    <p class="contact__row">0411 837 260
      <svg class="icon" width="18" height="26" viewBox="0 0 18 26" aria-hidden="true">
        <path d="M5,1 L9,7 L6,10 C7,14 9,17 12,19 L15,16 L18,21 L14,25 C6,23 1,13 1,5 Z" fill="var(--ink)"/>
      </svg>
    </p>
    <p class="contact__row contact__row--email">tidewaterridgepodiatry@pelmornmail.net
      <svg class="icon" width="24" height="17" viewBox="0 0 24 17" aria-hidden="true">
        <rect x="0" y="0" width="24" height="17" fill="var(--ink)"/>
        <path d="M1,1 L12,10 L23,1" fill="none" stroke="#fff" stroke-width="1.6"/>
      </svg>
    </p>
  </div>
</section>

</body>
</html>
```